Vormace

I need a professional web site that is directed at the energy industry, Oil, Gas, Mining
I need the website to have the usual pages
1. home page
2. news page.
3. contact us page
4. About us
and a CMS admin section to add further pages and content
Must be Google friendly with SEO facility

Target Market(s)

energy industry, Oil, Gas, Mining

Industry/Entity Type

Industry

Font styles to use
Sans Serif

Colors
faa54b
85cae6
cadf82

Requirements
Must have
• social media icons
site map

```html
<!DOCTYPE html>
<html lang="en">
<head>
<meta charset="utf-8">
<title>Vormace — Energy, Oil, Gas &amp; Mining</title>
<link href="https://fonts.googleapis.com/css2?family=Open+Sans:wght@400;600;700&family=Open+Sans+Condensed:wght@700&display=swap" rel="stylesheet">
<style>
:root{
  --orange:#faa54b;
  --orange-deep:#f08a1c;
  --blue:#85cae6;
  --green:#cadf82;
  --ink:#222326;
  --text:#7a7a7a;
  --muted:#a3a3a3;
  --line:#e4e4e4;
  --header-bg:#f1f1f1;
  --page-bg:#ffffff;
  --band-bg:#f3f3f3;
  --footer-bg:#2f3336;
  --footer-base:#25282b;
  --footer-text:#9aa0a4;
  --field-bg:#474c50;
}
*{box-sizing:border-box;margin:0;padding:0}
html,body{width:1200px;height:2175px;overflow:hidden}
body{position:relative;background:var(--page-bg);font-family:"Open Sans",Arial,sans-serif;color:var(--text)}
.abs{position:absolute}

/* header */
.site-header{position:absolute;left:0;top:0;width:1200px;height:87px;background:var(--header-bg);border-top:4px solid var(--orange)}
.brand{position:absolute;left:167px;top:22px;display:flex;align-items:center;gap:10px}
.brand-name{font-family:"Open Sans",sans-serif;font-weight:700;font-size:34px;letter-spacing:1px;color:var(--ink);text-transform:uppercase;line-height:1}
.brand-dot{width:16px;height:16px;border-radius:50%;background:var(--orange)}
.main-nav a{position:absolute;top:30px;font-size:15px;color:#333;text-decoration:none;text-transform:uppercase;letter-spacing:.3px}
.main-nav a.active{color:var(--orange-deep);border-bottom:2px solid var(--orange);padding-bottom:6px}
.nav-rule{position:absolute;left:511px;top:57px;width:500px;height:1px;background:#d8d8d8}

/* hero */
.hero{position:absolute;left:0;top:87px;width:1200px;height:451px;
  background:linear-gradient(180deg,#f7cf88 0%,#e9a05a 25%,#c9743a 50%,#8d4a22 75%,#3d1e0c 100%)}
.hero-caption{position:absolute;right:167px;top:488px;font-family:"Open Sans Condensed","Open Sans",sans-serif;font-weight:700;font-size:23px;color:#fff}

/* welcome */
.welcome-title{position:absolute;left:167px;top:588px;font-family:"Open Sans",sans-serif;font-weight:600;font-size:28px;color:var(--ink);display:flex;align-items:center;gap:10px}
.welcome-title .brand-inline{color:var(--orange-deep);font-weight:700;text-transform:uppercase;letter-spacing:1px}
.welcome-copy{position:absolute;left:167px;top:632px;width:522px;font-size:13.5px;line-height:24px;color:var(--text)}
.btn-primary{position:absolute;left:167px;top:761px;width:138px;height:36px;background:linear-gradient(#fbb05a,#f08a1c);border-radius:3px;color:#fff;font-weight:600;font-size:16px;text-align:center;line-height:36px;box-shadow:0 2px 3px rgba(0,0,0,.15)}
.video-frame{position:absolute;left:738px;top:600px;width:292px;height:200px;background:#fff;box-shadow:0 1px 6px rgba(0,0,0,.25);padding:4px}
.video-still{width:100%;height:100%;background:linear-gradient(180deg,#6a6fc4 0%,#8b78bf 40%,#d88a6a 75%,#3a2a40 100%);position:relative}
.video-bar{position:absolute;left:0;bottom:0;width:100%;height:22px;background:rgba(20,20,30,.85)}

/* section bands */
.band{position:absolute;left:0;width:1200px;background:linear-gradient(180deg,#fafafa,#f3f3f3)}
.band-rule{position:absolute;left:167px;width:866px;height:8px;background:linear-gradient(180deg,#e4e4e4,rgba(255,255,255,0))}
.section-title{position:absolute;left:0;width:1200px;text-align:center;font-family:"Open Sans Condensed","Open Sans",sans-serif;font-weight:700;font-size:26px;color:var(--ink)}
.section-title span{color:var(--orange-deep)}

/* services */
.service{position:absolute;top:944px;width:270px;text-align:center}
.service-icon{margin:0 auto;width:96px;height:96px}
.service-name{margin-top:26px;font-size:19px;font-weight:600}
.service-copy{margin-top:8px;font-size:13.5px;line-height:23px;color:var(--text)}
.btn-outline{display:inline-block;margin-top:18px;width:112px;height:32px;line-height:30px;border:1.5px solid;border-radius:3px;font-size:12px;text-transform:uppercase}
.mining .service-name,.mining .btn-outline{color:var(--orange-deep);border-color:var(--orange)}
.oil .service-name,.oil .btn-outline{color:var(--blue);border-color:var(--blue)}
.gas .service-name,.gas .btn-outline{color:var(--green);border-color:var(--green)}

/* news */
.news-card{position:absolute;top:1342px;width:268px}
.news-photo{position:relative;width:268px;height:159px}
.news-date{position:absolute;left:0;bottom:0;width:100%;height:30px;line-height:30px;padding-left:10px;background:rgba(0,0,0,.35);color:#fff;font-size:14px}
.news-title{margin-top:14px;font-size:16px;font-weight:600;color:var(--ink)}
.news-copy{margin-top:6px;font-size:13px;line-height:20px;color:var(--text)}
.news-more{margin-top:12px;font-size:12px;color:var(--muted);text-transform:uppercase}

/* testimonials */
.testimonial{position:absolute;top:1740px;width:400px}
.avatar{position:absolute;left:0;top:0;width:98px;height:98px;border-radius:50%;border:4px solid #fff;box-shadow:0 0 0 2px #ddd;background:radial-gradient(circle at 50% 40%,#d8d0c8,#9b948c)}
.quote-mark{position:absolute;left:74px;top:-2px;font-family:Georgia,serif;font-size:44px;line-height:1;color:var(--orange)}
.testimonial-body{position:absolute;left:115px;top:18px;width:285px;font-size:13px;line-height:22px;color:var(--muted)}
.testimonial-name{color:var(--orange-deep);font-size:14px}
.testimonial-role{font-size:12px;color:#b5b5b5}

/* footer */
.site-footer{position:absolute;left:0;top:1898px;width:1200px;height:238px;background:var(--footer-bg)}
.footer-col{position:absolute;top:32px;width:200px}
.footer-col h4{font-weight:400;font-size:17px;color:#c7cbce;padding-bottom:10px;border-bottom:1px solid #41464a;margin-bottom:12px}
.footer-col li{list-style:none;font-size:13px;line-height:26px;color:var(--footer-text)}
.contact-line{display:flex;gap:10px;font-size:13px;line-height:22px;color:var(--footer-text);margin-bottom:8px}
.field{width:196px;height:30px;background:var(--field-bg);border:none;margin-bottom:10px;padding-left:8px;font-size:12px;font-style:italic;color:#b8bcbf;line-height:30px}
.subscribe{display:flex}
.subscribe .field{width:154px}
.go-btn{width:40px;height:30px;background:var(--orange-deep);color:#fff;font-weight:700;font-size:13px;text-align:center;line-height:30px}
.social li{display:flex;align-items:center;gap:12px}
.social-dot{width:18px;height:18px;border-radius:50%;background:#8c9296}
.footer-base{position:absolute;left:0;top:2136px;width:1200px;height:39px;background:var(--footer-base);font-size:13px;color:var(--footer-text)}
.footer-base .copy{position:absolute;left:167px;top:10px}
.footer-base .copy strong{color:#d5d8da;font-weight:600}
.footer-base .legal{position:absolute;right:167px;top:10px}
</style>
</head>
<body>

<header class="site-header">
  <div class="brand"><span class="brand-name">Vormace</span><span class="brand-dot"></span></div>
  <nav class="main-nav">
    <a class="active" style="left:511px">Home</a>
    <a style="left:589px">About Us</a>
    <a style="left:694px">Our Services</a>
    <a style="left:825px">News</a>
    <a style="left:900px">Contact Us</a>
  </nav>
  <div class="nav-rule"></div>
</header>

<section class="hero" role="img" aria-label="Sunset over mountains with silhouettes of excavators and workers on a mining site"></section>
<p class="hero-caption">Lorem ipsum dolor sit amet, consectetur adipiscing elit.</p>

<h1 class="welcome-title">Welcome to <span class="brand-inline">Vormace</span></h1>
<p class="welcome-copy">Lorem ipsum dolor sit amet, consectetur adipiscing elit. Curabitur eu mauris est. Ut in facilisis augue. Sed tristique nisi erat, quis sodales est convallis vel. Fusce fermentum, magna id feugiat condimentum, leo eros varius est, in auctor purus lacus ultrices eros. Pellentes que volutpat urna eu venenatis aliquet. Sed ut dapibus ex. Sed sapien urna, tincidunt at felis sit amet, consequat imperdiet diam...</p>
<div class="btn-primary">READ MORE</div>

<div class="video-frame">
  <div class="video-still" role="img" aria-label="Video still of field workers at sunset">
    <svg class="abs" style="left:114px;top:62px" width="56" height="56" viewBox="0 0 56 56"><circle cx="28" cy="28" r="25" fill="none" stroke="#fff" stroke-width="4"/><path d="M22 17 L39 28 L22 39 Z" fill="#fff"/></svg>
    <div class="video-bar">
      <svg width="284" height="22" viewBox="0 0 284 22"><path d="M10 7 L16 11 L10 15 Z" fill="#ddd"/><rect x="26" y="9" width="190" height="4" fill="#555"/><rect x="26" y="9" width="40" height="4" fill="#aaa"/><rect x="236" y="8" width="28" height="6" fill="#777"/></svg>
    </div>
  </div>
</div>

<!-- services -->
<div class="band" style="top:858px;height:402px"></div>
<div class="band-rule" style="top:858px"></div>
<h2 class="section-title" style="top:892px">Our <span>Services</span></h2>

<div class="service mining" style="left:166px">
  <svg class="service-icon" viewBox="0 0 96 96" role="img" aria-label="Mining icon"><circle cx="48" cy="48" r="46" fill="#fff" stroke="var(--orange)" stroke-width="3"/><circle cx="48" cy="48" r="39" fill="var(--orange)"/></svg>
  <div class="service-name">Mining</div>
  <p class="service-copy">Lorem ipsum dolor sit amet, consectetur adipiscing elit. Curabitur eu mauris est. Ut in faci- lisis augue...</p>
  <span class="btn-outline">Read More</span>
</div>
<div class="service oil" style="left:465px">
  <svg class="service-icon" viewBox="0 0 96 96" role="img" aria-label="Oil icon"><circle cx="48" cy="48" r="46" fill="#fff" stroke="var(--blue)" stroke-width="3"/><circle cx="48" cy="48" r="39" fill="var(--blue)"/></svg>
  <div class="service-name">Oil</div>
  <p class="service-copy">Lorem ipsum dolor sit amet, consectetur adipiscing elit. Curabitur eu mauris est. Ut in faci- lisis augue...</p>
  <span class="btn-outline">Read More</span>
</div>
<div class="service gas" style="left:764px">
  <svg class="service-icon" viewBox="0 0 96 96" role="img" aria-label="Gas icon"><circle cx="48" cy="48" r="46" fill="#fff" stroke="var(--green)" stroke-width="3"/><circle cx="48" cy="48" r="39" fill="var(--green)"/></svg>
  <div class="service-name">Gas</div>
  <p class="service-copy">Lorem ipsum dolor sit amet, consectetur adipiscing elit. Curabitur eu mauris est. Ut in faci- lisis augue...</p>
  <span class="btn-outline">Read More</span>
</div>

<!-- news -->
<div class="band" style="top:1260px;height:393px"></div>
<div class="band-rule" style="top:1260px"></div>
<h2 class="section-title" style="top:1289px">Our <span>News</span></h2>

<article class="news-card" style="left:167px">
  <div class="news-photo" role="img" aria-label="Workers pushing a cart at sunset" style="background:linear-gradient(180deg,#5a5fb8,#a27ab0 45%,#e29a5e 75%,#4a3030)"><div class="news-date">26 December, 2014</div></div>
  <h3 class="news-title">Lorem ipsum dolor sit amet</h3>
  <p class="news-copy">Nulla hendrerit mattis eleifend. Phasellus varius lorem vitae cursus iaculis. Sed massa velit...</p>
  <div class="news-more">Read More →</div>
</article>
<article class="news-card" style="left:466px">
  <div class="news-photo" role="img" aria-label="Oil field pump jack with an engineer" style="background:linear-gradient(180deg,#3d5a7a,#7a8fa8 50%,#c79a7a 80%,#3a3530)"><div class="news-date">26 December, 2014</div></div>
  <h3 class="news-title">Lorem ipsum dolor sit amet</h3>
  <p class="news-copy">Nulla hendrerit mattis eleifend. Phasellus varius lorem vitae cursus iaculis. Sed massa velit...</p>
  <div class="news-more">Read More →</div>
</article>
<article class="news-card" style="left:765px">
  <div class="news-photo" role="img" aria-label="Gas processing plant with tanks and yellow pipework" style="background:linear-gradient(180deg,#3f7fc4,#8fb8dc 45%,#c8c8a0 70%,#6a7a3a)"><div class="news-date">26 December, 2014</div></div>
  <h3 class="news-title">Lorem ipsum dolor sit amet</h3>
  <p class="news-copy">Nulla hendrerit mattis eleifend. Phasellus varius lorem vitae cursus iaculis. Sed massa velit...</p>
  <div class="news-more">Read More →</div>
</article>

<!-- testimonials -->
<div class="band" style="top:1653px;height:245px"></div>
<div class="band-rule" style="top:1653px"></div>
<h2 class="section-title" style="top:1684px">Our <span>Testimonials</span></h2>

<svg class="abs" style="left:164px;top:1780px" width="16" height="22" viewBox="0 0 16 22"><path d="M13 2 L4 11 L13 20" fill="none" stroke="#9fc4de" stroke-width="3"/></svg>
<svg class="abs" style="left:1015px;top:1780px" width="16" height="22" viewBox="0 0 16 22"><path d="M3 2 L12 11 L3 20" fill="none" stroke="#9fc4de" stroke-width="3"/></svg>

<div class="testimonial" style="left:192px">
  <div class="avatar" role="img" aria-label="Client portrait"></div>
  <span class="quote-mark">“</span>
  <div class="testimonial-body">Lorem ipsum dolor sit amet, consectetur adipi- scing elit. Nam bibendum ..<div class="testimonial-name">Lorem ipsum</div><div class="testimonial-role">Lorem ipsum</div></div>
</div>
<div class="testimonial" style="left:610px">
  <div class="avatar" role="img" aria-label="Client portrait"></div>
  <span class="quote-mark">“</span>
  <div class="testimonial-body">Lorem ipsum dolor sit amet, consectetur adipi- scing elit. Nam bibendum ..<div class="testimonial-name">Lorem ipsum</div><div class="testimonial-role">Lorem ipsum</div></div>
</div>

<!-- footer -->
<footer class="site-footer">
  <div class="footer-col" style="left:167px">
    <h4>Usefull Links</h4>
    <ul><li>Home</li><li>About Us</li><li>Our services</li><li>News</li><li>Contact Us</li></ul>
  </div>
  <div class="footer-col" style="left:390px">
    <h4>Contact Us</h4>
    <div class="contact-line"><svg width="12" height="14" viewBox="0 0 12 14"><path d="M6 1 L11 7 L6 13 L1 7 Z" fill="#9aa0a4"/></svg><span>Lorem ipsum dolor sit amet,<br>consectetur 12345</span></div>
    <div class="contact-line"><svg width="12" height="14" viewBox="0 0 12 14"><rect x="3" y="1" width="7" height="12" rx="1" fill="none" stroke="#9aa0a4" stroke-width="1.5"/></svg><span>0800-555-0134</span></div>
    <div class="contact-line"><svg width="12" height="14" viewBox="0 0 12 14"><rect x="0" y="3" width="12" height="8" fill="#9aa0a4"/><path d="M0 3 L6 8 L12 3" fill="none" stroke="#2f3336" stroke-width="1"/></svg><span>info@vormace.com</span></div>
  </div>
  <div class="footer-col" style="left:615px">
    <h4>Join Us Now !</h4>
    <div class="field">Full Name</div>
    <div class="field">Phone no</div>
    <div class="subscribe"><div class="field">Enter your email</div><div class="go-btn">Go !</div></div>
  </div>
  <div class="footer-col" style="left:836px">
    <h4>Follow Us On</h4>
    <ul class="social">
      <li><span class="social-dot"></span>Sharebook</li>
      <li><span class="social-dot"></span>Chirper</li>
      <li><span class="social-dot"></span>Linkwork</li>
    </ul>
  </div>
</footer>
<div class="footer-base">
  <div class="copy">©2014 <strong>Vormace.com</strong> All rights reserved.</div>
  <div class="legal">Terms &amp; Conditions &nbsp;&nbsp;|&nbsp;&nbsp; Privacy Policy &nbsp;&nbsp;|&nbsp;&nbsp; Feedback</div>
</div>

</body>
</html>
```